Postcard Design

We are a full service lawn and landscape maintenance business. Employees are myself as owner-operator and
my son as operator and pesticide applicator and hardscape designer and builder along with myself as helper in the
hardscape. We have over 30 years experience and have operated as Doug's Yard Trimming for 23 years since 1993.
We are dependable and reasonably priced and hard working. My son is an excellent operator. We are full service year round. Spring cleanups, Summer all service, Fall cleanups and Winter snow removal.

Industry/Entity Type

Business

```html
<!DOCTYPE html>
<html lang="en">
<head>
<meta charset="utf-8">
<title>Doug's Yard Trimming – Postcard</title>
<link href="https://fonts.googleapis.com/css2?family=Jost:wght@400;500;700&family=Oswald:wght@400&family=Arimo:wght@700&display=swap" rel="stylesheet">
<style>
  :root{
    --page:#2b2b2b;
    --white:#ffffff;
    --ink:#23343a;
    --teal-band:rgba(40,120,140,.72);
    --call-band:#2fc7c9;
    --blue:#1e88c8;
    --cyan:#17d3f0;
    --green:#3cc84a;
    --banner:#0e8fcf;
    --fold:#2a2a2a;
    --line:#333333;
  }
  *{margin:0;padding:0;box-sizing:border-box}
  html,body{width:900px;height:1200px;overflow:hidden;background:var(--page)}
  body{position:relative;font-family:"Jost",sans-serif}
  .card{position:absolute;left:62px;width:775px;height:501px;overflow:hidden;background:var(--white)}
  .card--front{top:62px}
  .card--back{top:638px}
  .card svg.shapes{position:absolute;inset:0}
  .txt{position:absolute;color:var(--white)}

  /* front */
  .front-heading{right:25px;top:53px;text-align:right;font-size:27px;line-height:36px;font-weight:400}
  .front-year{right:25px;top:182px;text-align:right;font-size:25px;line-height:33px;font-weight:700}
  .service-list{position:absolute;right:25px;top:264px;list-style:none;text-align:right;color:var(--ink);font-size:21px;line-height:36px}
  .service-list li{display:block}
  .service-list li.two-line{line-height:28px;margin-top:6px}
  .service-list svg{display:inline-block;vertical-align:-1px;margin-right:4px}
  .call-line{right:25px;top:420px;font-family:"Oswald",sans-serif;font-size:25px;line-height:38px;display:flex;align-items:center;gap:8px}
  .business-name{left:73px;top:352px;font-family:"Arimo",sans-serif;font-weight:700;color:var(--white);line-height:42px}
  .business-name span{display:block}
  .business-name .n1{font-size:35px}
  .business-name .n2{font-size:32px}
  .business-name .n3{font-size:30px}

  /* back */
  .about{position:absolute;left:37px;color:var(--ink)}
  .about--caps{top:36px;font-size:15px;line-height:20px;font-weight:500;text-transform:uppercase}
  .about--s{top:86px;font-size:18px;line-height:22px}
  .about--m{top:134px;font-size:20px;line-height:24px}
  .about--l{top:171px;font-size:21px;line-height:28px;font-weight:500}
  .about--p{top:266px;font-size:17px;line-height:22px;font-weight:400}
  .stamp-box{position:absolute;left:667px;top:27px;width:83px;height:96px;border:1px solid var(--line)}
  .address-line{position:absolute;left:530px;width:220px;border-top:1px solid var(--line)}
  .contact-banner{position:absolute;left:0;top:368px;width:489px;height:100px;background:var(--banner);color:var(--white);font-size:34px;font-weight:500;line-height:100px;padding-left:78px}
</style>
</head>
<body>

<section class="card card--front">
  <svg class="shapes" width="775" height="501" viewBox="0 0 775 501">
    <defs>
      <linearGradient id="photo-front" x1="0" y1="0" x2="0" y2="1">
        <stop offset="0" stop-color="#8fc3ea"/>
        <stop offset=".45" stop-color="#c9c1ad"/>
        <stop offset=".7" stop-color="#7fae4a"/>
        <stop offset="1" stop-color="#5d9a2e"/>
      </linearGradient>
      <linearGradient id="panel-fill" x1="0" y1="0" x2="0" y2="1">
        <stop offset="0" stop-color="#4fd9f0"/>
        <stop offset=".45" stop-color="#5fdca0"/>
        <stop offset="1" stop-color="#8ae898"/>
      </linearGradient>
    </defs>
    <rect width="775" height="501" fill="url(#photo-front)" role="img" aria-label="Photo of a stone-fronted house with a neatly mown lawn and trimmed hedges"/>
    <path d="M425,0 C560,120 590,360 470,501 L775,501 L775,0 Z" fill="var(--blue)"/>
    <path d="M445,0 C575,120 605,360 490,501 L775,501 L775,0 Z" fill="var(--cyan)"/>
    <path d="M462,0 C590,120 620,360 505,501 L775,501 L775,0 Z" fill="url(#panel-fill)" opacity=".92"/>
    <rect x="400" y="32" width="375" height="10" fill="var(--green)" opacity=".8"/>
    <polygon points="410,46 775,46 775,166 470,166" fill="var(--teal-band)"/>
    <polygon points="405,416 775,416 775,461 430,461" fill="var(--call-band)"/>
    <rect x="440" y="461" width="335" height="12" fill="#6ee6f4"/>
  </svg>

  <div class="txt front-heading">We Are A Full Service<br>Lawn And Landscape<br>Maintenance</div>
  <div class="txt front-year">We Are Full Service<br>Year Round.</div>
  <ul class="service-list">
    <li><svg width="17" height="17" viewBox="0 0 17 17"><circle cx="8.5" cy="8.5" r="7.5" fill="none" stroke="#fff" stroke-width="1.5"/><path d="M5 8.8l2.4 2.4L12 6.3" fill="none" stroke="#fff" stroke-width="1.6"/></svg>Spring Cleanups</li>
    <li><svg width="17" height="17" viewBox="0 0 17 17"><circle cx="8.5" cy="8.5" r="7.5" fill="none" stroke="#fff" stroke-width="1.5"/><path d="M5 8.8l2.4 2.4L12 6.3" fill="none" stroke="#fff" stroke-width="1.6"/></svg>Summer All Service</li>
    <li class="two-line"><svg width="17" height="17" viewBox="0 0 17 17"><circle cx="8.5" cy="8.5" r="7.5" fill="none" stroke="#fff" stroke-width="1.5"/><path d="M5 8.8l2.4 2.4L12 6.3" fill="none" stroke="#fff" stroke-width="1.6"/></svg>Fall Cleanups &amp;<br>Winter Snow Removal</li>
  </ul>
  <div class="txt call-line">CALL US NOW
    <svg width="26" height="26" viewBox="0 0 26 26"><circle cx="13" cy="13" r="11.5" fill="none" stroke="var(--ink)" stroke-width="2"/><path d="M9 7.5l2 .2 1 3-1.4 1.2a8 8 0 0 0 3.5 3.5l1.2-1.4 3 1 .2 2c-.6 1-2 1.6-3.4 1.2A12 12 0 0 1 7.8 10.9C7.4 9.5 8 8.1 9 7.5z" fill="var(--ink)"/></svg>
    (123) 4567 890</div>
  <div class="txt business-name"><span class="n1">DOUG'S</span><span class="n2">YARD TRIMMING</span><span class="n3">SERVICES</span></div>
</section>

<section class="card card--back">
  <svg class="shapes" width="775" height="502" viewBox="0 0 775 502">
    <defs>
      <linearGradient id="photo-back" x1="0" y1="0" x2="0" y2="1">
        <stop offset="0" stop-color="#a9c9b4"/>
        <stop offset=".5" stop-color="#8fbf9a"/>
        <stop offset="1" stop-color="#6fa87a"/>
      </linearGradient>
      <linearGradient id="fold-shade" x1="0" y1="0" x2="1" y2="0">
        <stop offset="0" stop-color="#555555"/>
        <stop offset="1" stop-color="var(--fold)"/>
      </linearGradient>
    </defs>
    <rect width="775" height="502" fill="var(--white)"/>
    <path d="M0,0 L420,0 C540,110 560,360 450,502 L0,502 Z" fill="var(--cyan)"/>
    <path d="M0,0 L400,0 C522,110 540,360 432,502 L0,502 Z" fill="var(--green)"/>
    <path d="M0,0 L385,0 C505,110 522,360 417,502 L0,502 Z" fill="url(#photo-back)" role="img" aria-label="Close-up photo of a freshly mown striped lawn"/>
    <polygon class="ribbon-fold" points="489,468 489,474 374,492 392,468" fill="url(#fold-shade)"/>
  </svg>

  <div class="about about--caps">My son as operator and pesticide<br>applicator and hardscape designer</div>
  <div class="about about--s">And Builder Along With Myself As Helper<br>In The Hardscape.</div>
  <div class="about about--m">We Have Over 30 Years Experience</div>
  <div class="about about--l">And Have Operated As<br>Doug's Yard Trimming<br>For 23 Years Since 1993.</div>
  <div class="about about--p">We Are Dependable And Reasonably Priced<br>And Hard Working. My Son Is An<br>Excellent Operator.</div>

  <div class="stamp-box"></div>
  <div class="address-line" style="top:291px"></div>
  <div class="address-line" style="top:327px"></div>
  <div class="address-line" style="top:363px"></div>

  <div class="contact-banner">Contact Information</div>
</section>

</body>
</html>
```